Oversized Post Card for Busines Owners 1st 2nd and 3rd prizes

Create a professional, fresh and polished oversized post card for law firm specializing in Business Law, Succession Planning, and Employment Law

Use any picture(s) of your choice (mine or ones you recommend), logo, headshot and company info

www.morvenquaylegal.example

Westbrook Office - 4175 Hollister Avenue, Suite 1400, Charlotte, NC 28299
Kestrelmoor Office - 13840 Tamsin Way, Suite 300, Charlotte, NC 28296

Phone (704) 555-0187

Use this card for a Free Consultation

Target Market(s)

Business Owners (of small businesses)

Industry/Entity Type

Business

Font styles to use
Serif
Sans Serif

Requirements
Must have
• Company name, logo and contact info
• Serving business owners with legal guidance
• Business Law, Succession Planning & Wealth Transfers
• www.morvenquaylegal.example
• Westbrook Office - 4175 Hollister Avenue, Suite 1400, Charlotte, NC 28299
• Kestrelmoor Office - 13840 Tamsin Way, Suite 300, Charlotte, NC 28296
• Phone (704) 555-0187
• Use this card for a Free Consultation
Nice to have
• pictures (yours or mine) - you choose; headshot picture

```html
<!DOCTYPE html>
<html lang="en">
<head>
<meta charset="utf-8">
<title>Morven Quay Law, PLLC – Oversized Postcard</title>
<link rel="stylesheet" href="https://fonts.googleapis.com/css2?family=Cinzel:wght@400;600&family=Bebas+Neue&family=Open+Sans:wght@400;600&display=swap">
<style>
  :root {
    --navy: #0f3f60;
    --teal-blue: #1a7fa8;
    --box-blue: #15628c;
    --panel-grey: #f0f0f0;
    --mid-grey: #b9bbbd;
    --ink: #2f3337;
    --white: #ffffff;
    --page: #e4e5e7;
    --serif: "Cinzel", Georgia, serif;
    --condensed: "Bebas Neue", "Arial Narrow", sans-serif;
    --sans: "Open Sans", Arial, sans-serif;
  }
  * { box-sizing: border-box; margin: 0; padding: 0; }
  html, body { width: 896px; height: 1200px; overflow: hidden; background: var(--page); }
  .canvas { position: relative; width: 896px; height: 1200px; }
  .card {
    position: absolute; width: 750px; height: 486px; overflow: hidden;
    background: var(--white); box-shadow: 0 4px 14px rgba(0,0,0,.22);
  }
  .card-front { left: 50px; top: 53px; }
  .card-back { left: 97px; top: 668px; }
  .card svg.shapes { position: absolute; inset: 0; }
  .abs { position: absolute; }

  /* brand lockup */
  .brand { position: absolute; display: flex; align-items: center; gap: 14px; }
  .brand-dot { border-radius: 50%; background: var(--navy); flex: none; }
  .brand-name { font-family: var(--serif); font-weight: 400; color: var(--navy); line-height: 1; text-align: center; }
  .brand-name small { display: block; font-size: .42em; letter-spacing: .08em; margin-top: 4px; }
  .card-front .brand { left: 11px; top: 24px; }
  .card-front .brand-dot { width: 60px; height: 60px; }
  .card-front .brand-name { font-size: 29px; }
  .card-back .brand { left: 20px; top: 15px; }
  .card-back .brand-dot { width: 72px; height: 72px; }
  .card-back .brand-name { font-size: 35px; }

  /* front */
  .services { left: 31px; top: 148px; }
  .services-title { font-family: var(--condensed); font-weight: 400; font-size: 35px; color: var(--teal-blue); line-height: 1; margin-bottom: 12px; }
  .service-list { list-style: none; }
  .service-list li { display: flex; align-items: center; gap: 10px; font-family: var(--condensed); font-weight: 400; font-size: 31px; color: var(--navy); line-height: 1; height: 39px; }
  .service-list svg { flex: none; }
  .law-book { left: 262px; top: 332px; width: 116px; height: 84px; }
  .tagline { left: 400px; top: 38px; width: 350px; text-align: center; font-family: var(--serif); font-size: 25px; color: var(--white); line-height: 1.2; text-shadow: 0 1px 3px rgba(0,0,0,.5); }
  .contact-bar { left: 18px; top: 430px; display: flex; align-items: center; gap: 10px; font-family: var(--sans); font-weight: 600; font-size: 17px; color: var(--white); }
  .contact-bar .divider { width: 1px; height: 22px; background: var(--white); margin: 0 4px; }
  .contact-bar span { display: flex; align-items: center; gap: 6px; }

  /* back */
  .recognition { left: 15px; top: 115px; width: 400px; font-family: var(--sans); font-size: 12.5px; line-height: 18px; color: var(--ink); }
  .bio { left: 14px; top: 197px; width: 438px; font-family: var(--sans); font-size: 11.2px; line-height: 15.6px; color: var(--white); text-align: justify; }
  .signature { left: 270px; top: 345px; width: 180px; height: 30px; }
  .headshot { left: 23px; top: 356px; width: 104px; height: 117px; border: 3px solid var(--white); box-shadow: 0 1px 4px rgba(0,0,0,.3); }
  .firm-name { left: 145px; top: 397px; font-family: var(--sans); font-size: 13.5px; color: var(--ink); }
  .office { top: 421px; font-family: var(--sans); font-size: 10px; line-height: 14.5px; color: var(--ink); white-space: nowrap; }
  .office-west { left: 145px; }
  .office-kestrel { left: 320px; }
  .stamp { left: 628px; top: 34px; width: 103px; height: 81px; border: 1px solid #bfc1c3; }
  .free-consult { left: 539px; top: 449px; font-family: var(--sans); font-size: 11.5px; color: var(--ink); white-space: nowrap; }
</style>
</head>
<body>
<main class="canvas">

  <!-- FRONT -->
  <section class="card card-front">
    <svg class="shapes" width="750" height="486" viewBox="0 0 750 486">
      <defs>
        <linearGradient id="photoTone" x1="0" y1="0" x2="0" y2="1">
          <stop offset="0" stop-color="#7f8f7c"/>
          <stop offset=".45" stop-color="#a7b98a"/>
          <stop offset="1" stop-color="#8a8478"/>
        </linearGradient>
      </defs>
      <rect x="0" y="100" width="750" height="386" fill="var(--panel-grey)"/>
      <polygon points="350,0 392,0 480,486 434,486" fill="var(--navy)"/>
      <polygon points="392,0 750,0 750,486 480,486" fill="url(#photoTone)" role="img" aria-label="Photo: a green seedling growing from a glass jar filled with coins"/>
      <polygon points="0,410 518,410 510,486 0,486" fill="var(--navy)"/>
      <circle cx="552" cy="447" r="17" fill="var(--navy)"/>
      <circle cx="600" cy="447" r="17" fill="var(--navy)"/>
    </svg>

    <div class="brand">
      <span class="brand-dot"></span>
      <div class="brand-name">Morven Quay<small>LAW, PLLC</small></div>
    </div>

    <p class="abs tagline">Put Our Experience<br>To Work For You!</p>

    <div class="abs services">
      <h2 class="services-title">SERVING BUSINESS OWNERS</h2>
      <ul class="service-list">
        <li><svg width="22" height="22" viewBox="0 0 22 22"><circle cx="11" cy="11" r="11" fill="var(--teal-blue)"/><polygon points="8,6 16,11 8,16" fill="var(--white)"/></svg>LEGAL GUIDANCE</li>
        <li><svg width="22" height="22" viewBox="0 0 22 22"><circle cx="11" cy="11" r="11" fill="var(--teal-blue)"/><polygon points="8,6 16,11 8,16" fill="var(--white)"/></svg>BUSINESS LAW</li>
        <li><svg width="22" height="22" viewBox="0 0 22 22"><circle cx="11" cy="11" r="11" fill="var(--teal-blue)"/><polygon points="8,6 16,11 8,16" fill="var(--white)"/></svg>SUCCESSION PLANNING</li>
        <li><svg width="22" height="22" viewBox="0 0 22 22"><circle cx="11" cy="11" r="11" fill="var(--teal-blue)"/><polygon points="8,6 16,11 8,16" fill="var(--white)"/></svg>WEALTH TRANSFERS</li>
      </ul>
    </div>

    <div class="abs law-book" role="img" aria-label="Illustration: a law book with a wooden gavel" style="background:linear-gradient(160deg,#3a3a3c,#151516);border-radius:4px"></div>

    <div class="abs contact-bar">
      <span>
        <svg width="18" height="18" viewBox="0 0 24 24"><path d="M6.6 10.8a15.2 15.2 0 0 0 6.6 6.6l2.2-2.2c.3-.3.7-.4 1-.2 1.1.4 2.3.6 3.6.6.6 0 1 .4 1 1V20c0 .6-.4 1-1 1A17 17 0 0 1 3 4c0-.6.4-1 1-1h3.5c.6 0 1 .4 1 1 0 1.3.2 2.5.6 3.6.1.3 0 .7-.2 1z" fill="var(--white)"/></svg>
        (704) 555-0187
      </span>
      <i class="divider"></i>
      <span>
        <svg width="17" height="17" viewBox="0 0 24 24" fill="none" stroke="var(--white)" stroke-width="2"><circle cx="12" cy="12" r="10"/><ellipse cx="12" cy="12" rx="4.5" ry="10"/><line x1="2" y1="12" x2="22" y2="12"/></svg>
        www.morvenquaylegal.example
      </span>
    </div>
  </section>

  <!-- BACK -->
  <section class="card card-back">
    <svg class="shapes" width="750" height="486" viewBox="0 0 750 486">
      <polygon points="0,103 440,103 418,183 0,183" fill="var(--mid-grey)"/>
      <polygon points="0,183 460,183 491,379 0,379" fill="var(--box-blue)"/>
      <polygon points="0,379 462,379 494,486 0,486" fill="var(--mid-grey)"/>
      <polygon points="466,0 507,0 447,183 418,183" fill="var(--navy)"/>
      <polygon points="458,379 490,379 527,486 494,486" fill="var(--navy)"/>
      <g stroke="#c9cbcd" stroke-width="1">
        <line x1="502" y1="195" x2="729" y2="195"/>
        <line x1="502" y1="230" x2="729" y2="230"/>
        <line x1="502" y1="264" x2="729" y2="264"/>
        <line x1="502" y1="299" x2="729" y2="299"/>
        <line x1="502" y1="333" x2="729" y2="333"/>
      </g>
    </svg>

    <div class="brand">
      <span class="brand-dot"></span>
      <div class="brand-name">Morven Quay<small>LAW, PLLC</small></div>
    </div>

    <p class="abs recognition">Morven was named "40 Under 40" by Queen City Business Review and recognized by Enterprise Leader Magazine as a "Women Extraordinaire".</p>

    <p class="abs bio">As a Trusts and Estates Attorney, Morven Quay advises clients regarding estate planning, special needs planning, guardianships, probate, estate administration, estate disputes, trust administration, trust and fiduciary disputes, estate tax, income tax, gift tax, succession planning, and other business law matters. As a North Carolina Board Certified Specialist in Estate Planning and Probate law, Morven Quay provides legal guidance to high net worth individuals, as well as business owners, professional athletes, authors, lawyers, physicians, CPA’s, executives, professionals, individuals, and families with special needs.</p>

    <div class="abs signature" role="img" aria-label="Handwritten signature" style="background:linear-gradient(90deg,rgba(255,255,255,.18),rgba(255,255,255,.08))"></div>

    <div class="abs headshot" role="img" aria-label="Headshot portrait of the attorney" style="background:linear-gradient(180deg,#3b3f45,#c9a878 55%,#2a2c30)"></div>

    <p class="abs firm-name">Morven Quay Law, PLLC</p>
    <p class="abs office office-west">Westbrook Towers<br>4175 Hollister Avenue, Suite 1400<br>Charlotte, NC 28299</p>
    <p class="abs office office-kestrel">Kestrelmoor Office<br>13840 Tamsin Way, Suite 300<br>Charlotte, NC 28296</p>

    <div class="abs stamp"></div>
    <p class="abs free-consult">Use this card for a Free Consultation</p>
  </section>

</main>
</body>
</html>
```